KV Group

We need a new website for our company and since we had a very good work done for our logo in this site, we're back for the entire job.

Our company name is Marlowe Capital Group. We're adding files of examples of what we have done today. In my opinion we need a more attention lock in the site but yet financial simple work.

Our files (attached) will let you know what we have so far. We need a complete change but the colours should be the same, however you can change them not running away to far from the original, and of course matching with the logo.

We need examples for 3 kind of layouts.

- A HOME welcome layout
- An internal Layout with sidebar
- And internal Layout wide

We can buy image licenses if needed for assets.
Actually there are 5 slide images placed on the Welcome HOME, we need those there, but you can improve with better images to match the new website!!!

Target Market(s)

Clients looking for financial advisers, tax and funds specialist, currency advisers

Industry/Entity Type

Financial

Requirements
Must have
• all the fonts must be in accordance with the financial market sites........the welcome home page must be precise, neat and information accurate........the menu should be elegant........main focus on the Home page, should be also the PRIVATE ACCESS box log in.......

```html
<!DOCTYPE html>
<html lang="en">
<head>
<meta charset="utf-8">
<title>Marlowe Capital Group</title>
<link href="https://fonts.googleapis.com/css2?family=Oswald:wght@400;500&family=Roboto:wght@400;500&family=Open+Sans:wght@400;600&display=swap" rel="stylesheet">
<style>
:root{
  --orange:#f07c22;
  --orange-dark:#c85f10;
  --brown:#5a3212;
  --brown-dark:#3e200a;
  --cream:#f1eee7;
  --ink:#2b2b2b;
  --body:#555;
  --footer:#454545;
  --footer-dark:#333;
  --footer-base:#262626;
  --footer-link:#ddd;
  --badge-fill:#e4e4e4;
  --white:#fff;
}
*{box-sizing:border-box;margin:0;padding:0}
html,body{width:824px;height:1200px;overflow:hidden}
body{position:relative;background:var(--white);font-family:"Open Sans",sans-serif;color:var(--body)}
h1,h2,h3,h4{font-weight:400}
.abs{position:absolute}

/* header */
.header{left:0;top:0;width:824px;height:132px;background:var(--cream);border-top:3px solid var(--orange)}
.brand{left:89px;top:50px;display:flex;align-items:center;gap:8px}
.brand-mark{width:22px;height:22px;background:var(--orange)}
.brand-name{font-family:"Roboto",sans-serif;font-weight:500;font-size:17px;color:var(--ink);letter-spacing:.3px}
.access-tip{left:550px;top:12px;width:120px;height:36px;background:#333;border-radius:4px;color:var(--white);font-family:"Roboto",sans-serif;font-weight:500;font-size:12px;display:flex;align-items:center;justify-content:center;letter-spacing:.4px}
.access-tip::after{content:"";position:absolute;left:55px;bottom:-7px;border:7px solid transparent;border-bottom:0;border-top-color:#333}
.field{top:61px;width:119px;height:19px;background:var(--white);border:1px solid #d8d4cc;border-radius:3px;font-size:8px;font-style:italic;color:#999;padding:4px 7px}
.forgot{left:577px;top:93px;font-size:8px;font-style:italic;color:var(--orange)}
.login{left:686px;top:87px;width:48px;height:22px;background:var(--brown-dark);color:var(--white);font-family:"Roboto",sans-serif;font-size:9px;font-weight:500;border-radius:3px;display:flex;align-items:center;justify-content:center}

/* nav */
.nav{left:89px;top:116px;width:645px;height:31px;background:var(--orange);border-radius:3px;display:flex;justify-content:space-between;align-items:center;padding:0 13px;z-index:2}
.nav a{color:var(--white);text-decoration:none;font-family:"Roboto",sans-serif;font-weight:500;font-size:9px;letter-spacing:.2px}

/* hero */
.hero{left:0;top:132px;width:824px;height:278px;background:radial-gradient(ellipse at 55% 40%,#7a4a22 0%,var(--brown) 50%,var(--brown-dark) 100%)}
.slide{left:89px;top:176px;width:337px;height:188px;border:4px solid var(--white);background:linear-gradient(135deg,#c9d6e6 0%,#6c83a6 45%,#1e2f52 100%);box-shadow:0 10px 14px rgba(0,0,0,.35)}
.slide-btn{top:354px;width:20px;height:20px;border-radius:50%;background:var(--white);box-shadow:0 1px 3px rgba(0,0,0,.4)}
.hero-title{left:447px;top:170px;width:300px;font-family:"Oswald",sans-serif;font-weight:400;font-size:37px;line-height:38px;color:var(--white);text-transform:uppercase;letter-spacing:-.5px}
.hero-text{left:447px;top:253px;width:290px;font-size:11px;line-height:17px;color:var(--orange)}
.apply{left:447px;top:339px;width:106px;height:25px;background:var(--orange);color:var(--white);font-family:"Roboto",sans-serif;font-size:12px;font-weight:500;letter-spacing:.5px;border-radius:2px;display:flex;align-items:center;justify-content:center}

/* welcome */
.welcome-title{left:89px;top:427px;font-family:"Oswald",sans-serif;font-weight:400;font-size:19px;color:var(--orange)}
.welcome-text{left:89px;top:459px;width:640px;font-size:8.3px;line-height:16px}

/* service cards */
.card{top:535px;width:206px;height:248px;background:var(--white);box-shadow:0 1px 4px rgba(0,0,0,.18);border-radius:3px}
.card-head{position:absolute;left:0;top:0;width:206px;height:36px;background:linear-gradient(#c8641a,#a44b0c);border-radius:3px 3px 0 0;color:var(--white);font-family:"Oswald",sans-serif;font-weight:400;font-size:16px;display:flex;align-items:center;justify-content:center}
.card-head::after{content:"";position:absolute;left:85px;bottom:-14px;border:18px solid transparent;border-bottom:0;border-top:14px solid #a44b0c}
.card-img{position:absolute;left:7px;top:53px;width:192px;height:94px;border-radius:3px}
.card-text{position:absolute;left:8px;top:155px;width:190px;text-align:center;font-size:8.3px;line-height:16px}
.card-more{position:absolute;left:0;top:226px;width:206px;text-align:center;font-size:8px;color:#4a3a2a}

/* ticker */
.ticker{left:0;top:801px;width:824px;height:33px;background:#f3f2ee;border-top:2px solid #ddd;border-bottom:2px solid #ddd;display:flex;align-items:center;gap:18px;padding-left:100px;font-family:"Roboto",sans-serif;font-weight:500;font-size:7.5px;color:#1e2a55;white-space:nowrap;overflow:hidden}
.up{color:#1d8a18}.down{color:#d11}.flat{color:#e88a00}

/* verification band */
.verified{left:0;top:844px;width:824px;height:128px;background:var(--orange)}
.verified-title{left:0;top:856px;width:824px;text-align:center;font-family:"Oswald",sans-serif;font-weight:400;font-size:17px;color:var(--white)}
.badge{top:891px;width:121px;height:46px;background:var(--white);box-shadow:0 4px 5px rgba(0,0,0,.25);display:flex;align-items:center;justify-content:center}
.badge-shape{width:88px;height:24px;background:var(--badge-fill);border-radius:2px}

/* footer */
.footer{left:0;top:972px;width:824px;height:132px;background:var(--footer)}
.footer-col{top:990px}
.footer-col h4{font-family:"Roboto",sans-serif;font-weight:500;font-size:9.5px;color:var(--orange);margin-bottom:6px}
.footer-col a,.footer-col a:visited{display:block;color:var(--footer-link);text-decoration:none;font-size:8.3px;line-height:17px}
.footer-about{left:0;top:1104px;width:824px;height:66px;background:var(--footer-dark)}
.footer-about p{position:absolute;left:89px;top:8px;width:645px;font-size:7.3px;line-height:14px;color:#999}
.footer-base{left:0;top:1170px;width:824px;height:30px;background:var(--footer-base)}
.copyright,.legal{top:1182px;font-size:7.5px;color:#bbb}
.copyright{left:89px}
.legal{left:599px;width:136px;text-align:right}
</style>
</head>
<body>

<header class="abs header"></header>
<div class="abs brand"><span class="brand-mark"></span><span class="brand-name">Marlowe Capital Group</span></div>
<div class="abs access-tip">PRIVATE ACCESS!</div>
<div class="abs field" style="left:486px">Acc. Number</div>
<div class="abs field" style="left:616px">Acc. Password</div>
<div class="abs forgot">Forgot Acc.No/Password?</div>
<div class="abs login">LOG IN</div>

<nav class="abs nav">
  <a href="#">HOME</a><a href="#">ABOUT US</a><a href="#">INVESTMENTS</a><a href="#">FUNDS</a><a href="#">BROKERAGE</a><a href="#">EXCHANGE</a><a href="#">ACCOUNTS</a><a href="#">CONTACT US</a>
</nav>

<section class="abs hero"></section>
<div class="abs slide" role="img" aria-label="Business team reviewing documents at a desk"></div>
<div class="abs slide-btn" style="left:233px"><svg width="20" height="20" viewBox="0 0 20 20"><path d="M12 5 7 10l5 5" fill="none" stroke="#333" stroke-width="2.2"/></svg></div>
<div class="abs slide-btn" style="left:262px"><svg width="20" height="20" viewBox="0 0 20 20"><path d="M8 5l5 5-5 5" fill="none" stroke="#333" stroke-width="2.2"/></svg></div>
<h1 class="abs hero-title">Teamwork for your benefit !</h1>
<p class="abs hero-text">Aliquam molestie, mi et imperdiet euismod, dui purus auctor tellus, et interdum lacus lectus et ante. Sed accumsan sollicitudin sapien, sit amet adipiscing turpis gravida ac.</p>
<div class="abs apply">APPLY NOW</div>

<h2 class="abs welcome-title">Welcome to Our Site</h2>
<p class="abs welcome-text">Aliquam molestie, mi et imperdiet euismod, dui purus auctor tellus, et interdum lacus lectus et ante. Sed accumsan sollicitudin sapien, sit amet adipiscing turpis gravida ac. In congue, neque ac lobortis volutpat, libero mauris varius mi, vitae suscipit ipsum ligula vitae risus. Duis aliquam nibh a dui iaculis viverra id a velit. Vivamus egestas risus in magna varius commodo. Sed semper viverra egestas. Etiam pretium porttitor lectus, vel ornare neque porta volutpat.</p>

<article class="abs card" style="left:89px">
  <div class="card-head">Management &amp; Strategy</div>
  <div class="card-img" role="img" aria-label="Hand with pen over a bar chart report" style="background:linear-gradient(135deg,#f2f2f0 0%,#d9dcd8 55%,#a8c84a 100%)"></div>
  <p class="card-text">Aliquam molestie, mi et imperdiet euismod, dui purus auctor tellus, et interdum lacus lectus et ante. Sed accumsan sollicitudin sapien, sit amet adipiscing turpis gravida ac.</p>
  <div class="card-more">&lt;&lt; READ MORE &gt;&gt;</div>
</article>
<article class="abs card" style="left:309px">
  <div class="card-head">Funds</div>
  <div class="card-img" role="img" aria-label="Blue market figures over a world map" style="background:linear-gradient(135deg,#8ec3ee 0%,#2f7fd0 50%,#0f4ea8 100%)"></div>
  <p class="card-text">Aliquam molestie, mi et imperdiet euismod, dui purus auctor tellus, et interdum lacus lectus et ante. Sed accumsan sollicitudin sapien, sit amet adipiscing turpis gravida ac.</p>
  <div class="card-more">&lt;&lt; READ MORE &gt;&gt;</div>
</article>
<article class="abs card" style="left:527px">
  <div class="card-head">Currency Exchange</div>
  <div class="card-img" role="img" aria-label="Green buy and red sell keyboard keys" style="background:linear-gradient(90deg,#2f8a2a 0%,#3a9a2e 45%,#c0161a 55%,#a50f12 100%)"></div>
  <p class="card-text">Aliquam molestie, mi et imperdiet euismod, dui purus auctor tellus, et interdum lacus lectus et ante. Sed accumsan sollicitudin sapien, sit amet adipiscing turpis gravida ac.</p>
  <div class="card-more">&lt;&lt; READ MORE &gt;&gt;</div>
</article>

<div class="abs ticker">
  <span class="up">▲</span>
  <span>GBP/UAH = <span class="up">12.65761 ▲</span></span>
  <span>GBP/UGX = <span class="down">4010.06174 ▼</span></span>
  <span>GBP/USD = <span class="up">1.55817 ▲</span></span>
  <span>GBP/UYU = <span class="up">34.36026 ▲</span></span>
  <span>GBP/VEF = <span class="flat">0</span></span>
  <span>GBP/VUV = <span class="up">151.2</span></span>
</div>

<section class="abs verified"></section>
<h3 class="abs verified-title">Verified &amp; Protected by</h3>
<div class="abs badge" style="left:130px" role="img" aria-label="Partner certification badge"><span class="badge-shape"></span></div>
<div class="abs badge" style="left:273px" role="img" aria-label="Partner certification badge"><span class="badge-shape"></span></div>
<div class="abs badge" style="left:416px" role="img" aria-label="Partner certification badge"><span class="badge-shape"></span></div>
<div class="abs badge" style="left:559px" role="img" aria-label="Partner certification badge"><span class="badge-shape"></span></div>

<footer class="abs footer"></footer>
<div class="abs footer-col" style="left:89px"><h4>ABOUT US</h4><a href="#">History</a><a href="#">Expertize</a><a href="#">Identity</a><a href="#">Strategy</a><a href="#">Contact Us</a></div>
<div class="abs footer-col" style="left:186px"><h4>INVESTMENTS</h4><a href="#">History</a><a href="#">Expertize</a><a href="#">Identity</a><a href="#">Strategy</a><a href="#">Contact Us</a></div>
<div class="abs footer-col" style="left:302px"><h4>FUNDS</h4><a href="#">History</a><a href="#">Expertize</a><a href="#">Identity</a><a href="#">Strategy</a><a href="#">Contact Us</a></div>
<div class="abs footer-col" style="left:400px"><h4>CURRENCY EXCHANGE</h4><a href="#">History</a><a href="#">Expertize</a><a href="#">Identity</a><a href="#">Strategy</a><a href="#">Contact Us</a></div>
<div class="abs footer-col" style="left:549px"><h4>BROKERAGE</h4><a href="#">History</a><a href="#">Expertize</a><a href="#">Identity</a><a href="#">Strategy</a><a href="#">Contact Us</a></div>
<div class="abs footer-col" style="left:664px"><h4>ACCOUNTS</h4><a href="#">History</a><a href="#">Expertize</a><a href="#">Identity</a><a href="#">Strategy</a><a href="#">Contact Us</a></div>

<div class="abs footer-about"><p>Aliquam molestie, mi et imperdiet euismod, dui purus auctor tellus, et interdum lacus lectus et ante. Sed accumsan sollicitudin sapien, sit amet adipiscing turpis gravida ac. In congue, neque ac lobortis volutpat, libero mauris varius mi, vitae suscipit ipsum ligula vitae risus.Duis aliquam nibh a dui iaculis viverra id a velit. Vivamus egestas risus in magna varius commodo. Sed semper viverra egestas. Etiam pretium porttitor lectus, vel ornare neque porta volutpat.</p></div>
<div class="abs footer-base"></div>
<div class="abs copyright">Copyright © 2013. KV Group. All Right Reserved</div>
<div class="abs legal">Legal Diclaimer &nbsp;|&nbsp; Privacy Policy</div>

</body>
</html>
```